Business card design needed

This is a new business and a unique service.
The market is academic staff at universities in Australia.
The services include workshops, seminars, individual research planning, individual support to develop grant applications for major funding. I will travel to work with people or work electronically with individuals. I have a highly successful track record and am known in many universities for work done in the past.

Target Market(s)

university professorial staff and junior academic staff in australia

Industry/Entity Type

Travel

Contact Information for Business Card

The Scholar Compass
Opening Doors to Study Grants

Dr Linda J Prell

www.scholarcompass.com.au
E: info@scholarcompass.com.au
Ph: 0437 862049

Requirements
Must have
• I want a classic simple design. Colours - clean shades of blue with a contrast (not browns or orange).
I want to see line used as the primary feature, diagonal or other acute angles through part of the card.
Fonts should be crisp, angular and highly readable. Use upper and lower case in all text (except email and web address)
A simple logo based on TSC would be good.
Card can be designed vertically if the design works best that way.

```html
<!DOCTYPE html>
<html lang="en">
<head>
<meta charset="utf-8">
<title>The Scholar Compass – Business Card</title>
<link rel="stylesheet" href="https://fonts.googleapis.com/css2?family=Michroma&family=Source+Sans+3:wght@400&display=swap">
<style>
  :root {
    --card-blue: #0d4ba0;
    --sheen-white: #ffffff;
    --text-white: #ffffff;
  }
  * { margin: 0; padding: 0; box-sizing: border-box; }
  html, body {
    width: 1200px;
    height: 693px;
    overflow: hidden;
    background: var(--card-blue);
  }
  .card {
    position: relative;
    width: 1200px;
    height: 693px;
    background: var(--card-blue);
    overflow: hidden;
  }
  .card__sheen {
    position: absolute;
    inset: 0;
    width: 1200px;
    height: 693px;
  }
  .card__identity {
    position: absolute;
    left: 0;
    right: 0;
    top: 296px;
    text-align: center;
    color: var(--text-white);
  }
  .card__name {
    font-family: "Michroma", sans-serif;
    font-weight: 400;
    font-size: 31px;
    line-height: 1;
    letter-spacing: 3px;
    text-transform: uppercase;
  }
  .card__tagline {
    margin-top: 22px;
    font-family: "Source Sans 3", sans-serif;
    font-weight: 400;
    font-size: 35px;
    line-height: 1;
  }
</style>
</head>
<body>
  <main class="card">
    <svg class="card__sheen" viewBox="0 0 1200 693" aria-hidden="true">
      <defs>
        <linearGradient id="sheen-wide" x1="0" y1="0" x2="925" y2="0" gradientUnits="userSpaceOnUse">
          <stop offset="0" stop-color="var(--card-blue)" stop-opacity="0"/>
          <stop offset="0.15" stop-color="#3a63a8"/>
          <stop offset="1" stop-color="#ffffff"/>
        </linearGradient>
        <linearGradient id="sheen-edge" x1="327" y1="0" x2="905" y2="0" gradientUnits="userSpaceOnUse">
          <stop offset="0" stop-color="var(--card-blue)"/>
          <stop offset="0.35" stop-color="#5a79b8"/>
          <stop offset="1" stop-color="#ffffff"/>
        </linearGradient>
      </defs>
      <polygon class="sheen sheen--wide" points="0,0 925,0 925,38 0,99" fill="url(#sheen-wide)"/>
      <polygon class="sheen sheen--edge" points="327,0 1200,0 1200,17 327,133" fill="url(#sheen-edge)"/>
      <polygon class="sheen sheen--light" points="905,0 1200,0 1200,17 905,56" fill="#ffffff"/>
    </svg>

    <section class="card__identity">
      <h1 class="card__name">The Scholar Compass</h1>
      <p class="card__tagline">Opening Doors to Study Grants</p>
    </section>
  </main>
</body>
</html>
```